Brightwell Care Partners, LLC Business Card update!

would like a classier business card. Our cards currently just have our logo and contact information. Need better use of color and creativity
Logo attached.

Target Market(s)

Potential clients, contacts, existing clients. We are a consulting company

Industry/Entity Type

Business

Contact Information for Business Card

We like our colors but just have a boring card with our logo and a white background. I want something that stands out.

Colors
ec1f27
757575

Requirements
Must have
• Color to stay consistent. Logo provided
Nice to have
• Just better use of color/ design

```html
<!DOCTYPE html>
<html lang="en">
<head>
<meta charset="utf-8">
<title>Brightwell Care Partners – Business Card</title>
<link rel="stylesheet" href="https://fonts.googleapis.com/css2?family=Exo+2:wght@400;500;600&display=swap">
<style>
  :root {
    --brand-red: #ec1f27;
    --brand-grey: #757575;
    --ink-dark: #2b2b2b;
    --page-bg: #e9e7e4;
    --white: #ffffff;
  }
  html, body {
    margin: 0;
    padding: 0;
    width: 1200px;
    height: 1174px;
    overflow: hidden;
    background: var(--page-bg);
    font-family: "Exo 2", Arial, sans-serif;
  }
  .canvas {
    position: relative;
    width: 1200px;
    height: 1174px;
  }
  .card {
    position: absolute;
    left: 250px;
    width: 700px;
    height: 400px;
    overflow: hidden;
    box-shadow: 0 6px 18px rgba(0,0,0,0.18);
  }
  .card--front { top: 150px; }
  .card--back { top: 624px; }
  .card-art {
    position: absolute;
    inset: 0;
    width: 700px;
    height: 400px;
  }
  .brand {
    position: absolute;
    display: flex;
    align-items: center;
    gap: 12px;
    color: var(--brand-red);
    font-weight: 500;
  }
  .brand-dot {
    width: 34px;
    height: 34px;
    border-radius: 50%;
    background: var(--brand-red);
    flex: none;
  }
  .brand-name {
    font-size: 30px;
    line-height: 1.05;
    letter-spacing: 0.5px;
  }
  .card--front .brand { left: 20px; top: 228px; }
  .card--back .brand { left: 26px; top: 40px; }
  .person {
    position: absolute;
    right: 50px;
    top: 200px;
    text-align: right;
    color: var(--ink-dark);
  }
  .person-name {
    font-size: 22px;
    font-weight: 600;
    letter-spacing: 1.5px;
  }
  .person-title {
    font-size: 10px;
    font-weight: 600;
    letter-spacing: 1px;
    margin-top: 2px;
  }
  .contact-list {
    position: absolute;
    left: 30px;
    top: 258px;
    margin: 0;
    padding: 0;
    list-style: none;
    color: var(--white);
    font-size: 13px;
    letter-spacing: 1px;
  }
  .contact-list li {
    display: flex;
    align-items: center;
    gap: 10px;
    height: 23px;
  }
  .contact-list li.small { font-size: 12px; letter-spacing: 0.4px; height: 19px; }
  .contact-icon { width: 13px; height: 13px; fill: var(--white); flex: none; }
  .address {
    position: absolute;
    right: 32px;
    top: 320px;
    text-align: right;
    color: var(--white);
    font-size: 15px;
    font-style: normal;
    line-height: 1.55;
    letter-spacing: 0.8px;
  }
</style>
</head>
<body>
<main class="canvas">

  <section class="card card--front">
    <svg class="card-art" viewBox="0 0 700 400" aria-hidden="true">
      <defs>
        <linearGradient id="silver-front" x1="0" x2="1" y1="0" y2="0">
          <stop offset="0" stop-color="#f4f4f4"/>
          <stop offset="0.45" stop-color="#b9b9b9"/>
          <stop offset="0.7" stop-color="#ffffff"/>
          <stop offset="1" stop-color="#757575"/>
        </linearGradient>
        <radialGradient id="panel-front" cx="0.6" cy="0.5" r="0.7">
          <stop offset="0" stop-color="#fbfbfb"/>
          <stop offset="1" stop-color="#dcdcdc"/>
        </radialGradient>
      </defs>
      <rect width="700" height="400" fill="var(--brand-red)"/>
      <path d="M0,128 C200,98 340,140 450,200 C545,252 625,270 700,270 L700,400 L0,400Z" fill="var(--white)"/>
      <path d="M0,146 C200,118 340,158 450,218 C545,270 625,286 700,286 L700,400 L0,400Z" fill="url(#silver-front)"/>
      <path d="M0,160 C200,134 340,174 450,234 C545,286 625,300 700,300 L700,400 L0,400Z" fill="url(#panel-front)"/>
    </svg>
    <div class="brand">
      <span class="brand-dot"></span>
      <span class="brand-name">Brightwell<br>Care Partners</span>
    </div>
  </section>

  <section class="card card--back">
    <svg class="card-art" viewBox="0 0 700 400" aria-hidden="true">
      <defs>
        <linearGradient id="silver-back" x1="0" x2="1" y1="0" y2="0">
          <stop offset="0" stop-color="#ffffff"/>
          <stop offset="0.35" stop-color="#a9a9a9"/>
          <stop offset="0.65" stop-color="#d8d8d8"/>
          <stop offset="1" stop-color="#757575"/>
        </linearGradient>
        <radialGradient id="panel-back" cx="0.55" cy="0.35" r="0.75">
          <stop offset="0" stop-color="#ffffff"/>
          <stop offset="1" stop-color="#d9d9d9"/>
        </radialGradient>
      </defs>
      <rect width="700" height="400" fill="url(#panel-back)"/>
      <path d="M0,214 C150,198 300,212 430,246 C545,276 625,290 700,290 L700,400 L0,400Z" fill="var(--white)"/>
      <path d="M0,228 C150,214 300,228 430,262 C545,292 625,304 700,304 L700,400 L0,400Z" fill="url(#silver-back)"/>
      <path d="M0,240 C150,228 300,242 430,276 C545,306 625,316 700,316 L700,400 L0,400Z" fill="var(--brand-red)"/>
    </svg>

    <div class="brand">
      <span class="brand-dot"></span>
      <span class="brand-name">Brightwell<br>Care Partners</span>
    </div>

    <div class="person">
      <div class="person-name">DANIEL REYES</div>
      <div class="person-title">MANAGING DIRECTOR</div>
    </div>

    <ul class="contact-list">
      <li>
        <svg class="contact-icon" viewBox="0 0 16 16" aria-label="Phone"><path d="M3 1l3 3-2 2c1 2 3 4 5 5l2-2 3 3-2 3C7 15 1 9 1 3z"/></svg>
        012 555 0198
      </li>
      <li>
        <svg class="contact-icon" viewBox="0 0 16 16" aria-label="Mobile"><path d="M4 0h8v16H4zM5.5 2v10h5V2zM7 13h2v2H7z" fill-rule="evenodd"/></svg>
        012 555 0199
      </li>
      <li>
        <svg class="contact-icon" viewBox="0 0 16 16" aria-label="Fax"><path d="M4 1h7v4H4zM1 6h14v9H1zM3 8v2h4V8zM10 8h2v2h-2zM10 11h2v2h-2z" fill-rule="evenodd"/></svg>
        012 555 0197
      </li>
      <li class="small">
        <svg class="contact-icon" viewBox="0 0 16 16" aria-label="Email"><path d="M1 3h14v10H1zM2 4l6 5 6-5z" fill-rule="evenodd"/></svg>
        hello@brightwellcare.com
      </li>
      <li class="small">
        <svg class="contact-icon" viewBox="0 0 16 16" aria-label="Website"><circle cx="8" cy="8" r="6.5" fill="none" stroke="#fff" stroke-width="1.3"/><ellipse cx="8" cy="8" rx="2.8" ry="6.5" fill="none" stroke="#fff" stroke-width="1.1"/><path d="M1.5 8h13" stroke="#fff" stroke-width="1.1"/></svg>
        www.brightwellcare.com
      </li>
    </ul>

    <address class="address">
      214, 9th floor, Harbor Plaza<br>
      Elmstead Road NVK
    </address>
  </section>

</main>
</body>
</html>
```